Companies Need AI to Deal with AI

Seeking to do an pellorama look and feel to express the following narrative in a creative clever way: Artificial intelligence (AI) is significantly changing and disrupting a wide range of industries, including industrials, agriculture, finance, and more. AI can drive new solutions at a far lower cost and shorter time frames than traditional companies. New entrants have even beaten the initial wave of disruptors at their own game. Companies need AI to rise up to the challenge of AI, but to understand and adopt AI requires a fundamental rethink of their mindset and approach.
Target Market(s)
Age group 20-30+ year olds.
Colors
Designer to choose colors to be used in the design.
Requirements
Must have
- creative clever way of using images and graphics. Must make people think wow - how unique and cool is this!
Should not have
- any image of brains.

```html
<!DOCTYPE html>
<html lang="en">
<head>
<meta charset="utf-8">
<title>Companies Need AI to Deal with AI</title>
<link rel="stylesheet" href="https://fonts.googleapis.com/css2?family=Jost:wght@700&display=swap">
<style>
  :root {
    --bg-light: #ffffff;
    --bg-mid: #ececec;
    --bg-edge: #cfcfcf;
    --ink: #111111;
    --accent: #e8481e;
    --robot-white: #f2f2f2;
    --robot-grey: #a9a9a9;
    --robot-blue: #2d55c9;
    --robot-red: #d9471d;
    --chrome-light: #d6d9dc;
    --chrome-dark: #1c1d20;
  }
  html, body {
    margin: 0;
    padding: 0;
    overflow: hidden;
  }
  .poster {
    position: relative;
    width: 1200px;
    height: 1200px;
    overflow: hidden;
    background: radial-gradient(circle at 52% 40%, var(--bg-light) 0%, var(--bg-mid) 55%, var(--bg-edge) 100%);
  }
  .robots {
    position: absolute;
    inset: 0;
    width: 1200px;
    height: 1200px;
  }
  .headline {
    position: absolute;
    top: 58px;
    left: 330px;
    width: 600px;
    margin: 0;
    text-align: center;
    font-family: "Jost", "Futura", sans-serif;
    font-weight: 700;
    font-size: 96px;
    line-height: 108px;
    letter-spacing: 2px;
    text-transform: uppercase;
    color: var(--ink);
  }
  .headline .line {
    display: block;
  }
  .headline .accent {
    color: var(--accent);
  }
</style>
</head>
<body>
<main class="poster">
  <svg class="robots" viewBox="0 0 1200 1200" aria-hidden="false">
    <defs>
      <linearGradient id="team-light" x1="0" y1="0" x2="1" y2="0">
        <stop offset="0" stop-color="var(--robot-grey)"/>
        <stop offset="0.35" stop-color="var(--robot-white)"/>
        <stop offset="0.6" stop-color="var(--robot-blue)"/>
        <stop offset="1" stop-color="var(--robot-red)"/>
      </linearGradient>
      <linearGradient id="team-chrome" x1="0" y1="0" x2="1" y2="1">
        <stop offset="0" stop-color="var(--chrome-light)"/>
        <stop offset="0.45" stop-color="#5d6166"/>
        <stop offset="1" stop-color="var(--chrome-dark)"/>
      </linearGradient>
    </defs>
    <path class="robot-team robot-team--light" role="img"
          aria-label="Illustration: a row of glossy white, blue and red robots seen from behind, facing right"
          d="M0 230 C120 170 330 200 430 300 C520 390 560 520 560 640 L560 1200 L0 1200 Z"
          fill="url(#team-light)"/>
    <path class="robot-team robot-team--chrome" role="img"
          aria-label="Illustration: a group of dark chrome and glass robots facing left toward the white robots"
          d="M1200 60 C1020 50 880 170 840 330 C800 470 700 560 690 700 L690 1200 L1200 1200 Z"
          fill="url(#team-chrome)"/>
  </svg>

  <h1 class="headline">
    <span class="line">Companies</span>
    <span class="line">Need <span class="accent">AI</span></span>
    <span class="line">To Deal</span>
    <span class="line">With</span>
    <span class="line accent">AI</span>
  </h1>
</main>
</body>
</html>
```